Simple "top list" webpage (LiftYourBand.net)

Project Overview
The goal of the project is to make a webpage that shows a « top list » of artists which are currently raising funds on crowdfunding websites such as crowdtunely, fanstakerhouse, …
Visitors and artist’s producers will be able to vote for theirs artists
by 2 possibilities :
- 1 vote each day
- Buy a pack of a dozen vote for a limited amount of time
The more an artist has votes, the more he must be visible on the list to attract others producers.
Deliverables Required :
We need 2 types of deliverables for this project, to get full
webdesign package (no database backend, scripting, etc, ...) :
- A Logo (typography and/or image):
o 1 Image with logo + website name together
o 1 Image with image only (if it is chosen to make a
image+text logo…)
- A website design
o 1 html page with the general layout of the front page with the artist list
o Collection of images included in the design
Technical Requirements :
- No flash
- W3C stantards compliant
Audience
The audience profile is very heterogeneous, however :
- Music fans (style can be anything)
- Artists supporters
- Artist funders
- Talents anticipers
Tone
The global design should be modern and simple.
A typical visit will last no more than 1 minute, therefore the design shouldn’t distract too much the visitor. He must get straight to the
important information : the artist list.
Details :
The page should present a list of approximatively 15 artists (with
potential of other pages to get to the next ones)
Each Artist area should present the following informations
Artist Photo
Artist name
Fund raised (and maybe % of completion of fund raising)
Number of producers
Crowdfunding Platform
Number of votes
Tendency of votes (climbing, flat, down)
Reason: Hi All,
Thanks for all your quality submissions. As we are getting more designs, I extend deadlines in order to provide more feedback on submission.
Thanks again a lot.
Hugo

```html
<!DOCTYPE html>
<html lang="en">
<head>
<meta charset="utf-8">
<title>top list – Artist Chart</title>
<link href="https://fonts.googleapis.com/css2?family=Open+Sans:wght@400;600;700&display=swap" rel="stylesheet">
<style>
:root{
  --page-bg:#1c1c1c;
  --stripe:#262626;
  --header:#151515;
  --nav:#2a2a2a;
  --white:#ffffff;
  --ink:#222222;
  --muted:#8a8a8a;
  --rule:#d2d2d2;
  --accent:#b8125f;
  --photo:#3a3330;
  --video:#111111;
  --footer:#000000;
  --social:#2f6fb8;
}
*{box-sizing:border-box;margin:0;padding:0}
html,body{width:1093px;height:1200px;overflow:hidden}
body{
  position:relative;
  font-family:"Open Sans",Verdana,sans-serif;
  background:repeating-linear-gradient(135deg,var(--page-bg) 0 22px,var(--stripe) 22px 44px);
  color:var(--ink);
}
.page{position:absolute;left:143px;top:0;width:801px;height:1113px;background:var(--white)}
.page-fade{position:absolute;left:0;right:0;top:1036px;height:77px;background:linear-gradient(#fff,#d9d9d9)}
.masthead{position:absolute;left:148px;top:0;width:792px;height:83px;
  background:radial-gradient(ellipse at 70% 20%,#3a3a3a,var(--header) 70%)}
.site-name{position:absolute;left:29px;top:10px;font-size:48px;font-weight:400;color:#e8e8e8;letter-spacing:1px}
.search{position:absolute;left:620px;top:48px;width:133px;height:20px;background:#fff;border:1px solid #999;
  font-size:11px;color:#aaa;padding:2px 4px}
.search-icon{position:absolute;left:757px;top:48px}
.main-nav{position:absolute;left:148px;top:83px;width:792px;height:34px;background:var(--nav)}
.main-nav a{position:absolute;top:9px;font-size:12.5px;color:#fff;text-decoration:none}
.main-nav .current::after{content:"";position:absolute;left:50%;bottom:-11px;margin-left:-6px;
  border:6px solid transparent;border-bottom-color:#fff}
.artists{position:absolute;left:148px;top:134px;width:551px}
.artists h1{position:absolute;left:9px;top:10px;font-size:22px;font-weight:700;letter-spacing:.5px}
.artists .intro{position:absolute;left:9px;top:41px;width:535px;font-size:12.5px;line-height:15px;color:var(--muted)}
.rank-list{position:absolute;left:0;top:90px;width:551px;list-style:none;border-top:3px double var(--rule)}
.rank-row{position:relative;height:132px;border-bottom:3px double var(--rule)}
.rank-no{position:absolute;left:8px;top:44px;font-size:25px;color:var(--accent)}
.trend{position:absolute;left:40px;top:48px}
.artist-photo{position:absolute;left:79px;top:7px;width:238px;height:112px;border:1px solid #ccc;padding:4px;background:#fff;
  box-shadow:0 1px 2px rgba(0,0,0,.15)}
.artist-photo span{display:block;width:100%;height:100%;background:linear-gradient(180deg,#6d655e,var(--photo) 60%,#1b1918)}
.artist-name{position:absolute;left:325px;top:5px;font-size:13px;font-weight:700}
.vote-btn{position:absolute;left:480px;top:7px;width:59px;height:19px;background:var(--accent);color:#fff;
  font-size:11.5px;text-align:center;line-height:19px}
.votes{position:absolute;left:325px;top:24px;font-size:12px;color:var(--muted)}
.blurb{position:absolute;left:325px;top:42px;width:200px;font-size:12px;line-height:14px;color:var(--muted)}
.platform{position:absolute;left:325px;top:75px;font-size:12px;font-weight:700;color:#9a9a9a;letter-spacing:.5px}
.funds{position:absolute;left:325px;top:95px;width:112px;height:19px;background:var(--accent);color:#fff;
  font-size:12px;text-align:center;line-height:19px}
.pager{position:absolute;left:329px;top:1050px;font-size:15px;color:var(--ink)}
.pager a{color:var(--ink);text-decoration:underline;margin-right:3px}
.pager .on{color:var(--accent)}
.sidebar{position:absolute;left:704px;top:134px;width:236px;height:900px;border-left:3px double var(--rule)}
.side-block{position:absolute;left:0;width:236px;border-top:3px double var(--rule)}
.side-block h2{font-size:15px;font-weight:700;letter-spacing:.6px;margin:7px 0 0 8px}
.video{position:absolute;left:8px;top:35px;width:221px;height:160px;background:var(--video)}
.video-ctrl{position:absolute;left:8px;top:204px}
.post{margin:6px 0 0 11px;width:210px}
.post h3{font-size:12.5px;font-weight:400;color:var(--ink)}
.post .kicker{font-size:10.5px;color:#444;margin-top:2px}
.post p{font-size:12px;line-height:13.5px;color:var(--muted);margin-top:6px}
.footer{position:absolute;left:0;top:1113px;width:1093px;height:87px;background:var(--footer)}
.foot-nav{position:absolute;left:177px;top:21px;font-size:11.5px;color:#bbb;word-spacing:2px}
.foot-nav span{margin:0 14px}
.copyright{position:absolute;left:177px;top:44px;font-size:11.5px;color:#eee}
.follow{position:absolute;left:715px;top:22px;width:89px;height:22px;background:#bbb;color:#222;
  font-size:11.5px;font-weight:700;text-align:center;line-height:22px}
.social{position:absolute;top:25px;display:flex;align-items:center;gap:5px;font-size:12px;color:#fff}
.social i{display:block;width:14px;height:14px;background:var(--social)}
</style>
</head>
<body>
<div class="page"><div class="page-fade"></div></div>

<header class="masthead">
  <div class="site-name">top list</div>
  <div class="search">SEARCH</div>
  <svg class="search-icon" width="20" height="20" viewBox="0 0 20 20"><circle cx="8" cy="8" r="6" fill="none" stroke="#fff" stroke-width="2.5"/><line x1="12.5" y1="12.5" x2="18" y2="18" stroke="#fff" stroke-width="3"/></svg>
</header>

<nav class="main-nav">
  <a class="current" style="left:28px">HOME</a>
  <a style="left:104px">ABOUT</a>
  <a style="left:185px">BLOG</a>
  <a style="left:260px">NEWS</a>
  <a style="left:337px">CONTACT</a>
</nav>

<section class="artists">
  <h1>ARTISTS</h1>
  <p class="intro">Lorem ipsum dolor sit amet, consectetuer adipiscing elit. Aenean commodo ligula eget dolor. Aenean massa. Lum sociis natoque penatibus et magnis dis parturient montes, nascetur.</p>
  <ol class="rank-list">
    <li class="rank-row"><span class="rank-no">1.</span><svg class="trend" width="22" height="22" viewBox="0 0 22 22"><rect x="2" y="9" width="18" height="5" rx="1" fill="#444"/></svg><div class="artist-photo"><span role="img" aria-label="Band photo of four musicians"></span></div><span class="artist-name">Aenean commodo</span><span class="vote-btn">VOTE</span><span class="votes">10,753 Votes</span><p class="blurb">magnis dis parturient montes, nascetur ridiculus mus.</p><span class="platform">crowdtunely</span><span class="funds">$3,456 / $70,000</span></li>
    <li class="rank-row"><span class="rank-no">2.</span><svg class="trend" width="22" height="24" viewBox="0 0 22 24"><path d="M11 1 19 11H14V23H8V11H3Z" fill="#444"/></svg><div class="artist-photo"><span role="img" aria-label="Band photo of four musicians"></span></div><span class="artist-name">Aenean commodo</span><span class="vote-btn">VOTE</span><span class="votes">10,753 Votes</span><p class="blurb">magnis dis parturient montes, nascetur ridiculus mus.</p><span class="platform">crowdtunely</span><span class="funds">$3,456 / $70,000</span></li>
    <li class="rank-row"><span class="rank-no">3.</span><svg class="trend" width="22" height="24" viewBox="0 0 22 24"><path d="M11 23 19 13H14V1H8V13H3Z" fill="#444"/></svg><div class="artist-photo"><span role="img" aria-label="Band photo of four musicians"></span></div><span class="artist-name">Aenean commodo</span><span class="vote-btn">VOTE</span><span class="votes">10,753 Votes</span><p class="blurb">magnis dis parturient montes, nascetur ridiculus mus.</p><span class="platform">crowdtunely</span><span class="funds">$3,456 / $70,000</span></li>
    <li class="rank-row"><span class="rank-no">4.</span><svg class="trend" width="22" height="24" viewBox="0 0 22 24"><path d="M11 1 19 11H14V23H8V11H3Z" fill="#444"/></svg><div class="artist-photo"><span role="img" aria-label="Band photo of four musicians"></span></div><span class="artist-name">Aenean commodo</span><span class="vote-btn">VOTE</span><span class="votes">10,753 Votes</span><p class="blurb">magnis dis parturient montes, nascetur ridiculus mus.</p><span class="platform">crowdtunely</span><span class="funds">$3,456 / $70,000</span></li>
    <li class="rank-row"><span class="rank-no">5.</span><svg class="trend" width="22" height="22" viewBox="0 0 22 22"><rect x="2" y="9" width="18" height="5" rx="1" fill="#444"/></svg><div class="artist-photo"><span role="img" aria-label="Band photo of four musicians"></span></div><span class="artist-name">Aenean commodo</span><span class="vote-btn">VOTE</span><span class="votes">10,753 Votes</span><p class="blurb">magnis dis parturient montes, nascetur ridiculus mus.</p><span class="platform">crowdtunely</span><span class="funds">$3,456 / $70,000</span></li>
    <li class="rank-row"><span class="rank-no">6.</span><svg class="trend" width="22" height="24" viewBox="0 0 22 24"><path d="M11 1 19 11H14V23H8V11H3Z" fill="#444"/></svg><div class="artist-photo"><span role="img" aria-label="Band photo of four musicians"></span></div><span class="artist-name">Aenean commodo</span><span class="vote-btn">VOTE</span><span class="votes">10,753 Votes</span><p class="blurb">magnis dis parturient montes, nascetur ridiculus mus.</p><span class="platform">crowdtunely</span><span class="funds">$3,456 / $70,000</span></li>
  </ol>
</section>

<nav class="pager"><a>PREV</a> <a class="on">1</a> <a>2</a> <a>3</a> <a>4</a> <a>5</a> <a>6</a> <a>NEXT</a> <a>LAST</a></nav>

<aside class="sidebar">
  <section class="side-block" style="top:0;height:236px">
    <h2>FEATURED VIDEO</h2>
    <svg class="video" viewBox="0 0 221 160" role="img" aria-label="Featured video player"><rect width="221" height="160" fill="#111"/><path d="M95 65 122 81 95 97Z" fill="#fff"/></svg>
    <svg class="video-ctrl" width="221" height="14" viewBox="0 0 221 14"><path d="M0 2h2v10H0zM2 7l7-5v10zM9 7l7-5v10z" fill="#555"/><path d="M37 2l9 5-9 5z" fill="#555"/><path d="M55 2l7 5-7 5zM62 2l7 5-7 5zM69 2h2v10h-2z" fill="#555"/><rect x="86" y="1" width="135" height="12" fill="#333"/></svg>
  </section>
  <section class="side-block" style="top:239px;height:331px">
    <h2>NEWS</h2>
    <div class="post"><h3>Vivamus elementum</h3><div class="kicker">Integer tincidunt. Cras dapibus.</div><p>Vivamus elementum semper nisi. Aenean vulputate eleifend tellus. Aenean leo ligula, porttitor eu, consequat vitae, eleifend ac, enim. Aliquam lorem ante, dapibus in, viverra quis, feugiat a, tellus.</p></div>
    <div class="post"><h3>Vivamus elementum</h3><div class="kicker">Integer tincidunt. Cras dapibus.</div><p>Vivamus elementum semper nisi. Aenean vulputate eleifend tellus. Aenean leo ligula, porttitor eu, consequat vitae, eleifend ac, enim. Aliquam lorem ante, dapibus in, viverra quis, feugiat a, tellus.</p></div>
    <div class="post"><h3>Vivamus elementum</h3><div class="kicker">Integer tincidunt. Cras dapibus.</div></div>
  </section>
  <section class="side-block" style="top:570px;height:329px;border-bottom:3px double var(--rule)">
    <h2>BLOG</h2>
    <div class="post"><h3>Vivamus elementum</h3><div class="kicker">Integer tincidunt. Cras dapibus.</div><p>Vivamus elementum semper nisi. Aenean vulputate eleifend tellus. Aenean leo ligula, porttitor eu, consequat vitae, eleifend ac, enim. Aliquam lorem ante, dapibus in, viverra quis, feugiat a, tellus.</p></div>
    <div class="post"><h3>Vivamus elementum</h3><div class="kicker">Integer tincidunt. Cras dapibus.</div><p>Vivamus elementum semper nisi. Aenean vulputate eleifend tellus. Aenean leo ligula, porttitor eu, consequat vitae, eleifend ac, enim. Aliquam lorem ante, dapibus in, viverra quis, feugiat a, tellus.</p></div>
    <div class="post"><h3>Vivamus elementum</h3><div class="kicker">Integer tincidunt. Cras dapibus.</div></div>
  </section>
</aside>

<footer class="footer">
  <div class="foot-nav">HOME<span>I</span>ABOUT<span>I</span>BLOG<span>I</span>NEWS<span>I</span>CONTACT</div>
  <div class="copyright">Copyright © 2011 Northgate Web Designs</div>
  <div class="follow">Follow us on:</div>
  <div class="social" style="left:815px"><i></i>Friendsy</div>
  <div class="social" style="left:890px"><i></i>Chirpline</div>
</footer>
</body>
</html>
```